Sympathy Gift Supplier needs packaging designs

We provide sympathy/bereavement gifts such as memorial candles and picture frames for those who recently lost a loved one. We need packaging design for our boxes that will be uplifting and positive, yet elegant.

We have attached our logo in white and black as well as a saying we would like on the box, and what we need on the back panel.
Ignore the black as it was something we were working on for another product.

These products will be given as gifts to people who lost a loved one as remembrance.

• Back panel details (provided)
Memorial quote (provided)
Must be appropriate for this type of product

```html
<!DOCTYPE html>
<html lang="en">
<head>
<meta charset="utf-8">
<title>Serene Grove – Memorial Candle Box Panels</title>
<link rel="stylesheet" href="https://fonts.googleapis.com/css2?family=Allura&family=Open+Sans:wght@400;600;700&display=swap">
<style>
  :root {
    --page: #ffffff;
    --panel-front: #f6f8f2;
    --panel-back: #f6f6fa;
    --leaf-green: #7fa755;
    --leaf-green-soft: rgba(127, 167, 85, 0.55);
    --leaf-purple: #5e55a8;
    --leaf-purple-soft: rgba(94, 85, 168, 0.5);
    --gold: #e3a93c;
    --quote-green: #2f5d36;
    --accent-orange: #e0962e;
    --brand-purple: #5b2d8c;
  }
  * { box-sizing: border-box; margin: 0; padding: 0; }
  html, body {
    width: 803px; height: 1200px; overflow: hidden;
    background: var(--page);
  }
  .canvas { position: relative; width: 803px; height: 1200px; }

  .panel {
    position: absolute; left: 67px; width: 671px; height: 520px;
    overflow: hidden;
  }
  .panel--front { top: 59px; background: var(--panel-front); }
  .panel--back  { top: 618px; background: var(--panel-back); }

  .foliage { position: absolute; inset: 0; }
  .panel--front .foliage {
    background:
      radial-gradient(ellipse 190px 160px at 0% 0%, var(--leaf-green) 0%, var(--leaf-green-soft) 45%, transparent 100%),
      radial-gradient(ellipse 230px 120px at 100% 0%, var(--leaf-green-soft) 0%, transparent 100%),
      radial-gradient(ellipse 90px 260px at 100% 45%, var(--leaf-green-soft) 0%, transparent 100%),
      radial-gradient(ellipse 220px 190px at 0% 100%, var(--leaf-green) 0%, var(--leaf-green-soft) 40%, transparent 100%),
      radial-gradient(ellipse 260px 140px at 100% 100%, var(--leaf-green) 0%, var(--leaf-green-soft) 40%, transparent 100%),
      radial-gradient(ellipse 120px 80px at 45% 100%, rgba(227,169,60,0.35) 0%, transparent 100%),
      radial-gradient(ellipse 120px 80px at 30% 0%, rgba(227,169,60,0.35) 0%, transparent 100%);
  }
  .panel--back .foliage {
    background:
      radial-gradient(ellipse 190px 160px at 0% 0%, var(--leaf-purple) 0%, var(--leaf-purple-soft) 45%, transparent 100%),
      radial-gradient(ellipse 230px 120px at 100% 0%, var(--leaf-purple-soft) 0%, transparent 100%),
      radial-gradient(ellipse 90px 260px at 100% 45%, var(--leaf-purple-soft) 0%, transparent 100%),
      radial-gradient(ellipse 220px 190px at 0% 100%, var(--leaf-purple) 0%, var(--leaf-purple-soft) 40%, transparent 100%),
      radial-gradient(ellipse 260px 140px at 100% 100%, var(--leaf-purple) 0%, var(--leaf-purple-soft) 40%, transparent 100%),
      radial-gradient(ellipse 120px 80px at 45% 100%, rgba(227,169,60,0.35) 0%, transparent 100%),
      radial-gradient(ellipse 120px 80px at 30% 0%, rgba(227,169,60,0.35) 0%, transparent 100%);
  }

  .panel-content { position: absolute; inset: 0; text-align: center; }

  /* Front: memorial quote */
  .memorial-quote {
    position: absolute; left: 0; right: 0; top: 152px;
    font-family: "Allura", cursive;
    font-size: 44px; line-height: 46px;
    color: var(--quote-green);
  }
  .memorial-signoff {
    position: absolute; left: 0; right: 0; top: 340px;
    font-family: "Allura", cursive;
    font-size: 24px; color: var(--accent-orange);
  }

  /* Back: care information */
  .care-info {
    position: absolute; left: 0; right: 0; top: 100px;
    font-family: "Open Sans", sans-serif;
    color: var(--brand-purple);
  }
  .care-heading { font-size: 10px; font-weight: 700; letter-spacing: 0.2px; }
  .care-subheading { font-size: 7.5px; font-weight: 700; margin-top: 9px; }
  .care-text { font-size: 7.2px; line-height: 10px; margin-top: 3px; }
  .care-text--instructions { margin-top: 7px; }
  .origin { font-size: 10px; font-weight: 700; margin-top: 8px; }
  .divider {
    width: 140px; height: 1px; margin: 7px auto 0;
    background: var(--gold);
  }
  .brand-statement {
    position: absolute; left: 0; right: 0; top: 240px;
    font-family: "Allura", cursive;
    font-size: 21px; line-height: 24px;
    color: var(--brand-purple);
  }
  .brand-name {
    position: absolute; left: 0; right: 0; top: 355px;
    display: flex; align-items: center; justify-content: center; gap: 8px;
    font-family: "Open Sans", sans-serif; font-weight: 600;
    font-size: 20px; color: var(--brand-purple);
  }
  .brand-name__dot {
    width: 12px; height: 12px; border-radius: 50%;
    background: var(--brand-purple);
  }
  .brand-url {
    position: absolute; left: 0; right: 0; top: 412px;
    font-family: "Open Sans", sans-serif; font-weight: 700;
    font-size: 8.5px; letter-spacing: 0.3px;
    color: var(--brand-purple);
  }
</style>
</head>
<body>
<main class="canvas">

  <section class="panel panel--front">
    <div class="foliage" role="img" aria-label="Watercolour green leaf sprigs with gold outlined leaves framing the corners"></div>
    <div class="panel-content">
      <p class="memorial-quote">
        When the people we love<br>
        Are taken from us,<br>
        the way to have them live on<br>
        Is to never stop.
      </p>
      <p class="memorial-signoff">Loving Them.</p>
    </div>
  </section>

  <section class="panel panel--back">
    <div class="foliage" role="img" aria-label="Watercolour purple leaf sprigs with gold outlined leaves framing the corners"></div>
    <div class="panel-content">
      <div class="care-info">
        <h2 class="care-heading">WARNING</h2>
        <p class="care-text">Burn within sight. Keep away from flammable objects.<br>Keep away from children and pets.</p>
        <h3 class="care-subheading">Burning Instructions:</h3>
        <p class="care-text care-text--instructions">
          Trim wick to 1/4” before lighting. Keep candle free of any foreign<br>
          materials including matches and wick trimmings, Only burn the candle on a level,<br>
          fire resistant surface. Do not burn candle for more than<br>
          four hours at a time. Stop use when only 1/4” of wax remains.
        </p>
        <p class="origin">MADE IN CHINA</p>
        <div class="divider"></div>
      </div>
      <p class="brand-statement">
        Serene Grove is a family owned company<br>
        and all of our products are carefully designed and<br>
        crafted with your family in mind.
      </p>
      <div class="brand-name"><span class="brand-name__dot"></span>Serene Grove</div>
      <p class="brand-url">www.SereneGrove.com</p>
    </div>
  </section>

</main>
</body>
</html>
```